Business Card Design for Venture Kite

Venture Kite is a pro bono student consultancy service offered by Corvala KTRB to social start ups and enterprises. We provide consulting services with expertise in areas such as Marketing, IT, Business Strategy and Innovation.
I have attached\ the Venture Kite Logo here for your perusal.
Industry/Entity Type
Business
Contact Information for Business Card
Name: Ha Min Park Name: Thomas Leung
Role: Project Leader Role: Vice Project Leader
M:0477203941 M: 0479352806
E: ha-min.park@corvalaktrb.org E: thomas.leung@corvalaktrb.org
W: www.corvalaktrb.org W: www.corvalaktrb.org

```html
<!DOCTYPE html>
<html lang="en">
<head>
<meta charset="utf-8">
<title>Venture Kite — Business Card</title>
<link href="https://fonts.googleapis.com/css2?family=Oswald:wght@700&family=Questrial&display=swap" rel="stylesheet">
<style>
  :root {
    --backdrop: #e7e2da;
    --card-dark: #55585f;
    --card-dark-edge: #4a4d54;
    --card-light: #ffffff;
    --accent: #f2c318;
    --ink: #1c1c1e;
    --ink-on-dark: #f4f1ea;
  }
  * { box-sizing: border-box; margin: 0; padding: 0; }
  html, body { width: 1200px; height: 675px; overflow: hidden; }
  body {
    background: var(--backdrop);
    font-family: "Questrial", "Century Gothic", sans-serif;
    color: var(--ink);
  }
  .canvas {
    position: relative;
    width: 1200px;
    height: 675px;
    display: flex;
    justify-content: center;
    align-items: center;
    gap: 70px;
  }
  .card {
    position: relative;
    width: 340px;
    height: 550px;
    box-shadow: 0 10px 28px rgba(0,0,0,0.18);
    overflow: hidden;
  }
  .card-front {
    background: linear-gradient(160deg, var(--card-dark) 0%, var(--card-dark-edge) 100%);
  }
  .card-back { background: var(--card-light); }

  .accent-line {
    position: absolute;
    height: 3px;
    background: var(--accent);
  }
  .accent-line--top { top: 34px; left: 30px; right: 0; }
  .accent-line--bottom { bottom: 34px; left: 0; right: 30px; }

  .brand-name {
    font-family: "Oswald", "Arial Narrow", sans-serif;
    font-weight: 700;
    text-transform: uppercase;
    line-height: 1;
    letter-spacing: 0.02em;
  }
  .card-front .brand-name {
    position: absolute;
    top: 50%;
    left: 0;
    right: 0;
    transform: translateY(-50%);
    text-align: center;
    font-size: 50px;
    color: var(--ink-on-dark);
  }

  .card-back .brand-name {
    position: absolute;
    top: 62px;
    left: 0;
    right: 0;
    text-align: center;
    font-size: 30px;
    color: var(--ink);
  }

  .contact {
    position: absolute;
    top: 168px;
    left: 62px;
  }
  .contact-name {
    font-size: 21px;
    text-transform: uppercase;
    letter-spacing: 0.01em;
  }
  .contact-role {
    margin-top: 4px;
    margin-left: 22px;
    font-size: 9px;
    text-transform: uppercase;
    letter-spacing: 0.04em;
  }
  .contact-details {
    list-style: none;
    margin-top: 26px;
    font-size: 13.5px;
    line-height: 1.45;
  }
  .contact-rule {
    display: block;
    margin-top: 6px;
    margin-left: 22px;
    width: 48px;
    height: 1px;
    background: var(--ink);
  }
</style>
</head>
<body>
  <main class="canvas">
    <section class="card card-front" aria-label="Card front">
      <span class="accent-line accent-line--top"></span>
      <p class="brand-name">Venture Kite</p>
      <span class="accent-line accent-line--bottom"></span>
    </section>

    <section class="card card-back" aria-label="Card back">
      <p class="brand-name">Venture Kite</p>
      <div class="contact">
        <p class="contact-name">Ha Min Park</p>
        <p class="contact-role">Project Leader</p>
        <ul class="contact-details">
          <li>M: 0477203941</li>
          <li>E: ha-min.park@corvalaktrb.org</li>
          <li>W: www.corvalaktrb.org</li>
        </ul>
        <span class="contact-rule"></span>
      </div>
    </section>
  </main>
</body>
</html>
```